Copper Ridge Jerky packaging

We are looking for a modern, upmarket packaging for our range of beef jerky. Our existing logo is attached for your reference.
We aim to have our product placed in gastro pubs, craft beer events, bottle shops and hotels. The retail package itself will be 60g net and approximately 17cm x 14cm. There will be 4 flavours (original, chilli, smoked pepper and mongolian).
We would like to see some illustration in the design to showcase the different flavours. Use of colour and/or window is optional.

```html
<!DOCTYPE html>
<html lang="en">
<head>
<meta charset="utf-8">
<title>Copper Ridge Jerky – Chilli Flavoured Pack</title>
<link rel="stylesheet" href="https://fonts.googleapis.com/css2?family=Barlow+Condensed:wght@400;600;700&display=swap">
<style>
  :root {
    --page: #ffffff;
    --kraft: #c9a57c;
    --kraft-light: #d4b58f;
    --kraft-dark: #b8946b;
    --ink: #231f20;
    --chilli-red: #c8202a;
    --chilli-red-deep: #a8141d;
    --accent-red: #c4242c;
    --jerky-dark: #3a2128;
    --jerky-mid: #5a3038;
    --white: #ffffff;
  }
  * { margin: 0; padding: 0; box-sizing: border-box; }
  html, body {
    width: 995px; height: 1200px; overflow: hidden;
    background: var(--page);
    font-family: "Barlow Condensed", sans-serif;
  }
  .pack {
    position: absolute; left: 50px; top: 40px;
    width: 880px; height: 1107px;
    overflow: hidden;
    background: linear-gradient(160deg, var(--kraft-light), var(--kraft) 50%, var(--kraft-dark));
  }
  .pack-art { position: absolute; inset: 0; }
  .tagline {
    font-family: "Barlow Condensed", sans-serif;
    font-weight: 600; font-size: 27px; letter-spacing: 6px;
    fill: var(--accent-red);
  }
  .net-weight {
    position: absolute; left: 78px; top: 103px;
    width: 142px; height: 142px; border-radius: 50%;
    border: 3px solid var(--ink);
    display: flex; flex-direction: column; align-items: center; justify-content: center;
    color: var(--ink); line-height: 0.95;
  }
  .net-weight .amount { font-weight: 700; font-size: 48px; }
  .net-weight .label { font-weight: 400; font-size: 29px; }
  .brand-name {
    position: absolute; left: 197px; top: 282px; width: 500px;
    text-align: center; color: var(--ink); font-weight: 700;
    line-height: 0.85; letter-spacing: 8px;
  }
  .brand-name .line { display: block; font-size: 116px; }
  .brand-name .line.small { font-size: 60px; letter-spacing: 6px; margin-top: 22px; }
  .flavour-name {
    position: absolute; left: 190px; width: 500px; top: 905px;
    text-align: center; color: var(--white); line-height: 1;
  }
  .flavour-name .flavour { display: block; font-weight: 600; font-size: 84px; letter-spacing: 1px; }
  .flavour-name .descriptor { display: block; font-weight: 600; font-size: 53px; letter-spacing: 1px; }
</style>
</head>
<body>
  <div class="pack">
    <svg class="pack-art" width="880" height="1107" viewBox="0 0 880 1107">
      <defs>
        <linearGradient id="redBand" x1="0" y1="0" x2="1" y2="1">
          <stop offset="0" stop-color="var(--chilli-red)"/>
          <stop offset="1" stop-color="var(--chilli-red-deep)"/>
        </linearGradient>
        <linearGradient id="jerkyTone" x1="0" y1="0" x2="1" y2="1">
          <stop offset="0" stop-color="var(--jerky-mid)"/>
          <stop offset="1" stop-color="var(--jerky-dark)"/>
        </linearGradient>
        <radialGradient id="chilliTone" cx="0.5" cy="0.5" r="0.6">
          <stop offset="0" stop-color="#e8372f"/>
          <stop offset="1" stop-color="#d2262a" stop-opacity="0"/>
        </radialGradient>
        <clipPath id="bandClip">
          <polygon points="880,334 880,1107 84,1107"/>
        </clipPath>
        <path id="taglineArc" d="M 285 218 A 260 260 0 0 1 610 218"/>
      </defs>
      <polygon class="flavour-band" points="880,334 880,1107 84,1107" fill="url(#redBand)"/>
      <polygon class="product-window" role="img" aria-label="Photo of dried beef jerky pieces"
               points="263,514 443,694 226,911 34,710" fill="url(#jerkyTone)"/>
      <g clip-path="url(#bandClip)">
        <ellipse class="chilli-illustration" role="img" aria-label="Illustration of red chilli peppers"
                 cx="640" cy="740" rx="240" ry="150" fill="url(#chilliTone)"/>
      </g>
      <text class="tagline" text-anchor="middle">
        <textPath href="#taglineArc" startOffset="50%">PREMIUM CUTS</textPath>
      </text>
    </svg>

    <div class="net-weight">
      <span class="amount">60 G</span>
      <span class="label">NET</span>
    </div>

    <h1 class="brand-name">
      <span class="line">COPPER</span>
      <span class="line">RIDGE</span>
      <span class="line small">JERKY</span>
    </h1>

    <p class="flavour-name">
      <span class="flavour">CHILLI</span>
      <span class="descriptor">FLAVOURED</span>
    </p>
  </div>
</body>
</html>
```